Beer Can Label named: ZAP Ginger Beer

We need a funky design for a Ginger Beer that is made from all natural ingredients. The label needs to be full of Colour, emphasis on the Ginger Root. ZAP (Zested And Poured)

Target Market(s)

None beer drinkers'

Requirements
Must have
• Name on the label must beer easy to read. Needs to be very colourful, playful & even a bit cheaky.
Nice to have
• A label that looks at the benefits of Ginger for the body in a fun artistic design.
Should not have
• Should NOT be a simple, basic, minimalistic design

```html
<!DOCTYPE html>
<html lang="en">
<head>
<meta charset="utf-8">
<title>ZAP Ginger Beer – Label</title>
<link href="https://fonts.googleapis.com/css2?family=Bowlby+One&family=Open+Sans:wght@400;700&family=Italianno&display=swap" rel="stylesheet">
<style>
  :root {
    --yellow: #f7e91d;
    --yellow-light: #fdf7a6;
    --red: #b3161b;
    --green: #2e8a2c;
    --green-dark: #1f6b22;
    --orange: #f27a1a;
    --ink: #4a3a2a;
    --paper: #fffdf0;
    --white: #ffffff;
  }
  * { box-sizing: border-box; margin: 0; padding: 0; }
  html, body { width: 1200px; height: 1000px; overflow: hidden; background: var(--white); }
  .canvas { position: relative; width: 1200px; height: 1000px; }

  .label { position: absolute; top: 220px; width: 480px; height: 560px; overflow: hidden; }
  .label svg.label-bg { position: absolute; inset: 0; width: 100%; height: 100%; }
  .label--back { left: 80px; }
  .label--front { left: 640px; }

  /* Back label */
  .back-brand {
    position: absolute; left: 22px; top: 22px; width: 90px;
    font-family: "Bowlby One", sans-serif; font-size: 18px; line-height: 1.05;
    color: var(--red); text-align: center;
  }
  .benefits { position: absolute; left: 70px; top: 60px; width: 360px; text-align: center; color: var(--ink); }
  .benefits__title { font-family: "Italianno", cursive; font-size: 46px; color: var(--red); font-weight: 400; margin-bottom: 6px; }
  .benefit__name { font-family: "Open Sans", sans-serif; font-weight: 700; font-size: 15px; color: var(--orange); margin-top: 8px; }
  .benefit__text { font-family: "Open Sans", sans-serif; font-size: 12.5px; line-height: 1.3; }

  .purity-badge {
    position: absolute; left: 26px; top: 450px; width: 100px; height: 78px;
    background: var(--white); border: 4px solid var(--red); border-radius: 8px; overflow: hidden; text-align: center;
  }
  .purity-badge__value { font-family: "Bowlby One", sans-serif; font-size: 28px; color: var(--green); line-height: 46px; }
  .purity-badge__caption { background: var(--red); color: var(--yellow); font-family: "Open Sans", sans-serif; font-weight: 700; font-size: 13px; line-height: 26px; }

  .producer { position: absolute; left: 250px; top: 470px; color: var(--white); font-family: "Open Sans", sans-serif; }
  .producer__label { font-size: 18px; opacity: .85; }
  .producer__name { font-weight: 700; font-size: 17px; letter-spacing: .5px; }

  /* Front label */
  .front-title {
    position: absolute; left: 60px; top: 40px; width: 360px; text-align: center;
    font-family: "Bowlby One", sans-serif; color: var(--red); line-height: 1;
  }
  .front-title__brand { display: block; font-size: 92px; }
  .front-title__product { display: block; font-size: 54px; margin-top: 6px; }
  .ginger-root {
    position: absolute; left: 56px; top: 300px; width: 368px; height: 140px; border-radius: 60px 70px 40px 50px;
    background: radial-gradient(ellipse at 50% 45%, #f0dcb0 0%, #dcc08a 60%, rgba(220,192,138,0) 100%);
  }
</style>
</head>
<body>
<main class="canvas">

  <section class="label label--back" aria-label="Back label">
    <svg class="label-bg" viewBox="0 0 480 560" aria-hidden="true">
      <defs>
        <linearGradient id="backSky" x1="0" y1="0" x2="1" y2="1">
          <stop offset="0" stop-color="var(--yellow)"/>
          <stop offset="1" stop-color="var(--yellow-light)"/>
        </linearGradient>
      </defs>
      <rect width="480" height="560" fill="url(#backSky)"/>
      <rect x="0" y="0" width="480" height="14" fill="var(--red)"/>
      <path d="M0 400 Q240 330 480 380 L480 560 L0 560Z" fill="var(--red)"/>
      <path d="M0 420 Q240 360 480 400 L480 560 L0 560Z" fill="var(--green)"/>
      <rect x="56" y="50" width="392" height="370" rx="18" fill="var(--paper)" opacity=".92"/>
    </svg>

    <div class="back-brand">ZAP<br>GINGER<br>BEER</div>

    <div class="benefits">
      <h2 class="benefits__title">The Benefits</h2>
      <h3 class="benefit__name">Relieve Dizziness</h3>
      <p class="benefit__text">The symptoms of dizziness followed by nausea can be alleviated by consuming ginger.</p>
      <h3 class="benefit__name">Reducing Menstrual Pain</h3>
      <p class="benefit__text">For women who often feel pain during menstruation, you can try to consume as much as 500-2000 mg of ginger extract, for three days at the beginning of menstruation.</p>
      <h3 class="benefit__name">Osteoarthritis / Joint Aging</h3>
      <p class="benefit__text">According to a number of studies, pain due to this condition can be overcome by taking ginger extract.</p>
      <h3 class="benefit__name">Reducing Nausea &amp; Vomiting After Surgery</h3>
      <p class="benefit__text">The symptoms of dizziness followed by nausea can be alleviated by consuming ginger.</p>
    </div>

    <div class="purity-badge">
      <div class="purity-badge__value">100%</div>
      <div class="purity-badge__caption">Pure Ginger</div>
    </div>

    <div class="producer">
      <div class="producer__label">Produced by</div>
      <div class="producer__name">ZAP GINGER BEER</div>
    </div>
  </section>

  <section class="label label--front" aria-label="Front label">
    <svg class="label-bg" viewBox="0 0 480 560" aria-hidden="true">
      <defs>
        <radialGradient id="frontGlow" cx="0.85" cy="0.3" r="0.7">
          <stop offset="0" stop-color="var(--yellow-light)"/>
          <stop offset="1" stop-color="var(--yellow)"/>
        </radialGradient>
      </defs>
      <rect width="480" height="560" fill="url(#frontGlow)"/>
      <path d="M0 450 Q240 540 480 450 L480 560 L0 560Z" fill="var(--green)"/>
      <path d="M0 500 Q240 580 480 500 L480 560 L0 560Z" fill="var(--green-dark)" opacity=".5"/>
      <path d="M40 0 L40 340 Q40 480 240 480 Q440 480 440 340 L440 0" fill="none" stroke="var(--red)" stroke-width="14"/>
      <rect x="0" y="0" width="14" height="560" fill="var(--red)" opacity=".25"/>
      <rect x="466" y="0" width="14" height="560" fill="var(--red)" opacity=".25"/>
    </svg>

    <h1 class="front-title">
      <span class="front-title__brand">ZAP</span>
      <span class="front-title__product">GINGER<br>BEER</span>
    </h1>

    <div class="ginger-root" role="img" aria-label="Photograph of fresh ginger root with sliced pieces and green leaves"></div>
  </section>

</main>
</body>
</html>
```